Graphic design for "How It Works" for VelmoraStyles.com*

VelmoraStyles.com website is for selling custom designer outfits for women and girls in all countries, customers can choose existing designs on this website and customize to their measurements. Customers can also provide their own designs and measurements and our expert designers and tailors get the outfit stitched and delivered to the customer.

We wanted to explain how this entire process works in 4 steps in the form of graphic design with little heading and text describing each step.

Step 1: Select Dress
Its time to choose the beauty you want to adorn yourself with. We have a wide collection of premium dresses, colours and accessories. There is something for everyone! All you need to do is pick. If you can’t find what you are looking for then you can share a picture of what you want, we will get it done whatever you want.

Step 2: Customization
Everyone is different; hence we realise the need for customization of the design and size. Here you select exactly how you want your dress to be. From sleeves to cuts, everything will be done as per your wish. Enter your measurements, lo and behold! You’re done. Leave your comments for even more customization.

Step 3: Designer Consultation
We as a user-friendly brand, aspire to provide the best of services to our clients. Our expert lady designers will help you for everything right from selecting of fabric to design of dress to necessary accessories. Our designers are just a call away!

Step 4: Stitch and Deliver
After you have placed your order, we confirm and verify the details. The boutique completes your order, sends it to us and we deliver it to your doorstep. We also have a team of designers in-house to cater to your premium dressing needs.

```html
<!DOCTYPE html>
<html lang="en">
<head>
<meta charset="utf-8">
<title>How It Works</title>
<link href="https://fonts.googleapis.com/css2?family=Dosis:wght@400&family=Lilita+One&family=PT+Sans+Narrow&display=swap" rel="stylesheet">
<style>
  :root{
    --bg-top:#ffffff;
    --bg-bottom:#e9e9eb;
    --title:#c2457f;
    --purple:#7f58c4;
    --purple-dark:#53309a;
    --purple-deep:#3e1f80;
    --purple-light:#9a72d6;
    --magenta:#b01c78;
    --magenta-dark:#86105a;
    --magenta-deep:#6c0b48;
    --magenta-light:#e25aac;
    --red:#e2232e;
    --red-dark:#b3121c;
    --red-deep:#930c15;
    --red-light:#ef5a63;
    --blue:#2ba3dc;
    --blue-dark:#1a7fb8;
    --blue-deep:#136a9d;
    --blue-light:#4db6e6;
    --white:#ffffff;
  }
  *{margin:0;padding:0;box-sizing:border-box;}
  html,body{width:1200px;height:429px;overflow:hidden;}
  body{background:linear-gradient(var(--bg-top),var(--bg-bottom));position:relative;font-family:"PT Sans Narrow",sans-serif;}
  .connectors{position:absolute;left:0;top:0;width:1200px;height:429px;}
  .title{position:absolute;left:431px;top:24px;width:362px;text-align:center;font-family:"Dosis",sans-serif;font-weight:400;font-size:34px;letter-spacing:0.5px;color:var(--title);line-height:1;}
  .step{position:absolute;top:94px;width:175px;height:322px;border-radius:8px;color:var(--white);}
  .step svg.art{position:absolute;left:0;top:0;overflow:visible;}
  .step--select{left:135px;background:linear-gradient(160deg,var(--purple-light),var(--purple));}
  .step--custom{left:393px;background:linear-gradient(160deg,var(--magenta),var(--magenta-dark));}
  .step--consult{left:651px;background:linear-gradient(160deg,var(--red),var(--red-dark));}
  .step--deliver{left:904px;background:linear-gradient(160deg,var(--blue-light),var(--blue));}
  .step__copy{position:absolute;left:4px;right:4px;}
  .step__heading{font-family:"Lilita One",sans-serif;font-weight:400;font-size:14.5px;line-height:1;text-transform:uppercase;letter-spacing:0.1px;white-space:nowrap;margin-bottom:1px;}
  .step__text{font-size:11.6px;line-height:11px;text-align:justify;text-align-last:center;}
  .step--select .step__copy,.step--consult .step__copy{top:5px;}
  .step--custom .step__copy{top:209px;}
  .step--deliver .step__copy{top:212px;}
  .numeral{font-family:"Lilita One",sans-serif;fill:var(--white);}
  .numeral-label{font-family:"Lilita One",sans-serif;font-size:15px;}
</style>
</head>
<body>

<svg class="connectors" viewBox="0 0 1200 429" aria-hidden="true">
  <path d="M431 62 V30 Q431 21 440 21 H784 Q793 21 793 30 V62" fill="none" stroke="#c2457f" stroke-width="1"/>
  <path d="M431 62 H123 Q117 62 117 68 V204 Q117 210 123 210 H129" fill="none" stroke="#7f58c4" stroke-width="1" stroke-dasharray="3 2"/>
  <path d="M793 62 H1091 Q1097 62 1097 68 V204 Q1097 210 1091 210 H1084" fill="none" stroke="#2ba3dc" stroke-width="1" stroke-dasharray="3 2"/>
  <circle cx="431" cy="62" r="4" fill="#fff" stroke="#a0215f" stroke-width="2"/>
  <circle cx="793" cy="62" r="4" fill="#fff" stroke="#c4141f" stroke-width="2"/>
  <circle cx="129" cy="210" r="4" fill="#fff" stroke="#7f58c4" stroke-width="2"/>
  <circle cx="1084" cy="210" r="4" fill="#fff" stroke="#1a7fb8" stroke-width="2"/>
  <g>
    <rect x="483" y="66" width="30" height="2" fill="#7f58c4"/>
    <rect x="515" y="66" width="30" height="2" fill="#9b3f9f"/>
    <rect x="547" y="66" width="30" height="2" fill="#b01c78"/>
    <rect x="579" y="66" width="30" height="2" fill="#c2457f"/>
    <rect x="611" y="66" width="30" height="2" fill="#d7304a"/>
    <rect x="643" y="66" width="30" height="2" fill="#e2232e"/>
    <rect x="675" y="66" width="30" height="2" fill="#8c5aa6"/>
    <rect x="707" y="66" width="34" height="2" fill="#2ba3dc"/>
  </g>
</svg>

<h1 class="title">HOW IT WORKS</h1>

<section class="step step--select">
  <svg class="art" width="175" height="322" viewBox="0 0 175 322" aria-hidden="true">
    <polygon points="-12,172 -2,172 24,232 -2,292 -12,292 14,232" fill="var(--purple-light)"/>
    <polygon points="20,120 50,120 100,232 50,322 20,322 70,232" fill="var(--purple-deep)"/>
    <polygon points="50,150 70,150 112,232 70,310 50,310 92,232" fill="var(--purple-dark)"/>
    <rect x="74" y="176" width="92" height="112" rx="14" fill="#ffffff" opacity="0.12"/>
    <text class="numeral" x="72" y="283" font-size="140" textLength="94" lengthAdjust="spacingAndGlyphs">01</text>
    <rect x="78" y="200" width="16" height="60" rx="8" fill="var(--white)"/>
    <text class="numeral-label" fill="var(--purple)" transform="translate(92 256) rotate(-90)">STEP</text>
    <circle cx="187" cy="250" r="10" fill="var(--purple)"/>
    <circle cx="206" cy="250" r="7" fill="var(--purple)"/>
    <circle cx="220" cy="250" r="4.5" fill="var(--purple)"/>
  </svg>
  <div class="step__copy">
    <h2 class="step__heading">Select Dress</h2>
    <p class="step__text">Its time to choose the beauty you want to adorn yourself with. We have a wide collection of premium dresses, colours and accessories. There is something for everyone! All you need to do is pick. If you can’t find what you are looking for then you can share a picture of what you want, we will get it done whatever you want.</p>
  </div>
</section>

<section class="step step--custom">
  <svg class="art" width="175" height="322" viewBox="0 0 175 322" aria-hidden="true">
    <polygon points="-12,62 -2,62 24,122 -2,182 -12,182 14,122" fill="var(--magenta-light)"/>
    <polygon points="10,10 40,10 88,110 40,200 10,200 58,110" fill="var(--magenta-deep)"/>
    <polygon points="40,40 60,40 100,110 60,180 40,180 80,110" fill="var(--magenta-dark)"/>
    <rect x="72" y="38" width="94" height="100" rx="14" fill="#ffffff" opacity="0.12"/>
    <text class="numeral" x="70" y="130" font-size="125" textLength="98" lengthAdjust="spacingAndGlyphs">02</text>
    <rect x="76" y="56" width="16" height="60" rx="8" fill="var(--white)"/>
    <text class="numeral-label" fill="var(--magenta)" transform="translate(90 112) rotate(-90)">STEP</text>
    <circle cx="188" cy="75" r="10" fill="var(--magenta)"/>
    <circle cx="206" cy="76" r="7" fill="var(--magenta)"/>
    <circle cx="220" cy="76" r="4.5" fill="var(--magenta)"/>
  </svg>
  <div class="step__copy">
    <h2 class="step__heading">Customization</h2>
    <p class="step__text">Everyone is different; hence we realise the need for customization of the design and size. Here you select exactly how you want your dress to be. From sleeves to cuts, everything will be done as per your wish. Enter your measurements, lo and behold! You’re done. Leave your comments for even more customization.</p>
  </div>
</section>

<section class="step step--consult">
  <svg class="art" width="175" height="322" viewBox="0 0 175 322" aria-hidden="true">
    <polygon points="-12,172 -2,172 24,232 -2,292 -12,292 14,232" fill="var(--red-light)"/>
    <polygon points="10,120 40,120 90,232 40,322 10,322 60,232" fill="var(--red-deep)"/>
    <polygon points="40,150 60,150 102,232 60,310 40,310 82,232" fill="var(--red-dark)"/>
    <rect x="64" y="178" width="104" height="110" rx="14" fill="#ffffff" opacity="0.12"/>
    <text class="numeral" x="62" y="283" font-size="135" textLength="108" lengthAdjust="spacingAndGlyphs">03</text>
    <rect x="68" y="202" width="16" height="60" rx="8" fill="var(--white)"/>
    <text class="numeral-label" fill="var(--red)" transform="translate(82 258) rotate(-90)">STEP</text>
    <circle cx="188" cy="259" r="10" fill="var(--red)"/>
    <circle cx="206" cy="260" r="7" fill="var(--red)"/>
    <circle cx="220" cy="260" r="4.5" fill="var(--red)"/>
  </svg>
  <div class="step__copy">
    <h2 class="step__heading">Designer Consultation</h2>
    <p class="step__text">We as a user-friendly brand, aspire to provide the best of services to our clients. Our expert lady designers will help you for everything right from selecting of fabric to design of dress to necessary accessories. Our designers are just a call away!</p>
  </div>
</section>

<section class="step step--deliver">
  <svg class="art" width="175" height="322" viewBox="0 0 175 322" aria-hidden="true">
    <polygon points="-12,62 -2,62 24,122 -2,182 -12,182 14,122" fill="var(--blue-dark)"/>
    <polygon points="10,10 40,10 88,110 40,200 10,200 58,110" fill="var(--blue-deep)"/>
    <polygon points="40,40 60,40 100,110 60,180 40,180 80,110" fill="var(--blue-dark)"/>
    <rect x="58" y="30" width="110" height="108" rx="14" fill="#ffffff" opacity="0.12"/>
    <text class="numeral" x="56" y="130" font-size="135" textLength="111" lengthAdjust="spacingAndGlyphs">04</text>
    <rect x="62" y="52" width="16" height="60" rx="8" fill="var(--white)"/>
    <text class="numeral-label" fill="var(--blue)" transform="translate(76 108) rotate(-90)">STEP</text>
  </svg>
  <div class="step__copy">
    <h2 class="step__heading">Stitch and Deliver</h2>
    <p class="step__text">After you have placed your order, we confirm and verify the details. The boutique completes your order, sends it to us and we deliver it to your doorstep. We also have a team of designers in-house to cater to your premium dressing needs.</p>
  </div>
</section>

</body>
</html>
```